Garden Maintenance business card

I need a business card design for my new business "Copperleaf Outdoor Co". I do garden maintenance including lawns, turf lawn, pruning, hedging, water systems, anything related to the garden really (dont think i need to include any of that except garden maintenance)
Updates

Reason: narrowed it down and just showing my business partners the designs, cheers

Industry/Entity Type

Business

Requirements
Must have
• Must Have:
- ABN: XX XXX XXX XXX
Mobile phone number 00 0000000
email address xxxx.xxxxxx@quolmail.com
Owner Name Xxxx xxxxxx
title: garden specialist possibly under name or something sounding professional
logo which has been submitted both with a background and one without, feel free to choose whichever one you like
business name

```html
<!DOCTYPE html>
<html lang="en">
<head>
<meta charset="utf-8">
<title>Copperleaf Outdoor Co – Business Card</title>
<link rel="stylesheet" href="https://fonts.googleapis.com/css2?family=Saira+Condensed:wght@300;400&display=swap">
<style>
  :root {
    --card-orange: #f5821f;
    --card-white: #ffffff;
    --art-green: #8cc66a;
    --art-leaf: #2f4a2a;
    --art-skin: #e4ddd0;
  }
  html, body {
    margin: 0;
    padding: 0;
    width: 1200px;
    height: 750px;
    overflow: hidden;
    background: var(--card-white);
  }
  .card {
    position: relative;
    width: 1200px;
    height: 750px;
    overflow: hidden;
    background: var(--card-orange);
    font-family: "Saira Condensed", "Arial Narrow", sans-serif;
    font-weight: 300;
    color: var(--card-white);
  }
  .card__shape {
    position: absolute;
    inset: 0;
  }
  .identity {
    position: absolute;
    left: 72px;
    top: 92px;
    width: 450px;
  }
  .identity__name {
    margin: 0;
    font-size: 49px;
    font-weight: 300;
    line-height: 1;
    white-space: nowrap;
  }
  .identity__title {
    margin: 4px 0 0;
    text-align: right;
    font-size: 34px;
    line-height: 1;
    white-space: nowrap;
  }
  .business {
    position: absolute;
    left: 72px;
    top: 300px;
    margin: 0;
    font-size: 40px;
    font-weight: 400;
    line-height: 1;
    white-space: nowrap;
  }
  .contact {
    position: absolute;
    left: 72px;
    top: 514px;
    margin: 0;
    padding: 0;
    list-style: none;
    font-size: 40px;
    line-height: 58px;
    white-space: nowrap;
  }
</style>
</head>
<body>
  <main class="card">
    <svg class="card__shape" width="1200" height="750" viewBox="0 0 1200 750">
      <defs>
        <linearGradient id="art-tones" x1="0" y1="0" x2="0" y2="1">
          <stop offset="0" stop-color="var(--art-leaf)" stop-opacity="0.55"/>
          <stop offset="0.4" stop-color="var(--art-green)" stop-opacity="0.7"/>
          <stop offset="0.65" stop-color="var(--art-skin)"/>
          <stop offset="1" stop-color="var(--art-skin)"/>
        </linearGradient>
        <clipPath id="oval-clip">
          <ellipse cx="995" cy="512" rx="283" ry="378"/>
        </clipPath>
      </defs>
      <ellipse class="card__oval" cx="995" cy="512" rx="283" ry="378" fill="var(--card-white)"/>
      <g clip-path="url(#oval-clip)">
        <rect class="card__illustration" x="862" y="180" width="338" height="570" rx="40"
              fill="url(#art-tones)" role="img"
              aria-label="Illustration of a hand giving a thumbs up, with a small leafy sapling growing from a green-tinted thumb"/>
      </g>
    </svg>

    <header class="identity">
      <h1 class="identity__name">Owner Name Xxxx xxxxxx</h1>
      <p class="identity__title">garden specialist</p>
    </header>

    <p class="business">Copperleaf Outdoor Co</p>

    <ul class="contact">
      <li class="contact__abn">ABN: XX XXX XXX XXX</li>
      <li class="contact__mobile">Mobile: 00 0000000</li>
      <li class="contact__email">email: xxxx.xxxxxx@quolmail.com</li>
    </ul>
  </main>
</body>
</html>
```